Coral Beacon Stationery Design Project

I am looking for a suitable stationary design for my company Coral Beacon Pty Ltd (ACN 582 914 306).

The requirements can be better explained by visiting my website
"coral-beacon-trust.org"

I will be sending letters to Ministers of State and the Heads of Government Agencies so the theme needs to be formal and serious.

A theme with a shield or similar picking on the "guardian" concept would be appropriate

Target Market(s)

Ministers of State and Department Agency Heads and legal firms, the heads of Trustee Companies as well as Members of Coral Beacon

Industry/Entity Type

Government

Requirements
Must have
• Letterhead design is a priority - Business Card secondary

Must include tag line "Steady hands for every estate we tend" with a registered trade mark superscript at the end that is an R in a circle {Windows Alt +0174 on numeric keypad or Mac Option +R}.

Must include website address "Coral-Beacon-Trust.org" plus Email address "corbeacon@mailvessel.net

Company name "Coral Beacon Pty. Ltd." and Australian Company Number "ACN 582 914 306" needs to be shown more discretely

Address is "47 Finch Crescent, Marrowdale, 3291"
Nice to have
• A watermark is something to be considered

```html
<!DOCTYPE html>
<html lang="en">
<head>
<meta charset="utf-8">
<title>Coral Beacon Letterhead</title>
<link rel="stylesheet" href="https://fonts.googleapis.com/css2?family=PT+Sans:wght@400;700&family=Noto+Sans:wght@400&display=swap">
<style>
  :root {
    --brand-blue: #34459d;
    --brand-navy: #252b7c;
    --ink: #1c1c1c;
    --tag-ink: #2a2a2a;
    --paper: #ffffff;
  }
  * { margin: 0; padding: 0; box-sizing: border-box; }
  html, body { width: 849px; height: 1200px; overflow: hidden; background: var(--paper); }
  .letterhead { position: relative; width: 849px; height: 1200px; background: var(--paper); }

  .top-band {
    position: absolute; left: 0; top: 0; width: 849px; height: 26px;
    background: linear-gradient(to right, var(--brand-blue) 0 617px, var(--brand-navy) 617px 100%);
  }

  .brand { position: absolute; left: 42px; top: 48px; height: 58px; display: flex; align-items: center; }
  .brand-mark { width: 44px; height: 44px; border-radius: 50%; background: var(--brand-blue); }
  .brand-divider { width: 1.5px; height: 58px; background: var(--brand-blue); margin: 0 11px 0 12px; }
  .brand-name {
    font-family: "PT Sans", sans-serif; font-weight: 700; font-size: 31px;
    color: var(--brand-blue); letter-spacing: -0.2px; line-height: 1; margin-top: 12px;
  }

  .contact {
    position: absolute; left: 576px; top: 39px;
    font-family: "Noto Sans", sans-serif; font-size: 11.2px; line-height: 13.3px; color: var(--ink);
    display: grid; grid-template-columns: 38px auto; column-gap: 5px;
  }
  .contact dt { text-align: right; color: var(--brand-blue); }
  .contact dd { margin: 0; }

  .tagline {
    position: absolute; left: 0; width: 849px; top: 1160px; text-align: center;
    font-family: "PT Sans", sans-serif; font-size: 18.5px; color: var(--tag-ink);
    letter-spacing: -0.4px; padding-right: 20px;
  }
  .tagline sup { font-size: 13px; position: relative; top: -2px; vertical-align: super; line-height: 0; }

  .bottom-band {
    position: absolute; left: 0; top: 1187px; width: 849px; height: 13px;
    background: linear-gradient(to right, var(--brand-blue) 0 617px, var(--brand-navy) 617px 100%);
    text-align: center; padding-right: 20px;
    font-family: "Noto Sans", sans-serif; font-size: 10px; line-height: 13px; color: var(--paper);
  }
</style>
</head>
<body>
<main class="letterhead">
  <div class="top-band"></div>

  <header class="brand">
    <div class="brand-mark"></div>
    <div class="brand-divider"></div>
    <div class="brand-name">Coral Beacon</div>
  </header>

  <dl class="contact">
    <dt></dt><dd>Coral Beacon Pty Ltd.</dd>
    <dt></dt><dd>ACN 582 914 306</dd>
    <dt>e-mail</dt><dd>corbeacon@mailvessel.net</dd>
    <dt>web</dt><dd>www.coral-beacon-trust.org</dd>
    <dt>add</dt><dd>47 Finch Crescent,</dd>
    <dt></dt><dd>Marrowdale,3291</dd>
  </dl>

  <p class="tagline">Steady hands for every estate we tend<sup>®</sup></p>

  <footer class="bottom-band">www.coral-beacon-trust.org</footer>
</main>
</body>
</html>
```